The Bright Fern Studio Product Flyer for Trade Show

We are a small business that designs greeting cards/wall hangings. All our products are hand made using rolled strips of paper.
We are looking to showcase some of our card designs for a trade show this weekend. We want to include several of our images w/product number (on image or above/below), our business name, location and contact info and a brief description of our process. This will be for an 8.5"x11" single sided sheet of paper.

Target Market(s)

B2B Sales

Industry/Entity Type

Business

Font styles to use
Serif

Requirements
Must have
• Logo, Product Images w/numbers, Contact Info, Brief Description of process/pricing (.txt file), "10% off first order"
Nice to have
• Amazing color, sharp layout, even and professional appearance

```html
<!DOCTYPE html>
<html lang="en">
<head>
<meta charset="utf-8">
<title>The Bright Fern Studio – Product Flyer</title>
<link href="https://fonts.googleapis.com/css2?family=Cabin:wght@400;500;700&family=Oswald:wght@500;600&display=swap" rel="stylesheet">
<style>
  :root{
    --page:#e9edf1;
    --ink:#1c1c1c;
    --magenta:#e6168c;
    --leaf:#4e8a2e;
    --leaf-light:#8cc63f;
    --lime:#d6e824;
    --band-yellow:#eef07a;
    --badge-yellow:#f7ea18;
    --ribbon-red:#e8202a;
    --blue-deep:#1f78c9;
    --blue-light:#20a4e8;
    --white:#ffffff;
  }
  *{box-sizing:border-box;margin:0;padding:0}
  html,body{width:1200px;height:1200px;overflow:hidden;background:var(--page)}
  .flyer{
    position:absolute;left:177px;top:0;width:846px;height:1200px;overflow:hidden;
    font-family:"Cabin",sans-serif;color:var(--ink);
    background:
      radial-gradient(ellipse 420px 320px at 10% 42%, rgba(160,205,70,.55), transparent 70%),
      radial-gradient(ellipse 380px 300px at 95% 78%, rgba(240,140,190,.45), transparent 70%),
      radial-gradient(ellipse 380px 300px at 55% 88%, rgba(120,200,230,.40), transparent 70%),
      radial-gradient(ellipse 360px 260px at 88% 40%, rgba(200,170,230,.30), transparent 70%),
      radial-gradient(ellipse 400px 260px at 30% 15%, rgba(240,235,120,.55), transparent 70%),
      #fbfbf6;
  }
  .corner-pattern{position:absolute;border-radius:50%}
  .corner-pattern.left{left:-90px;top:-80px;width:300px;height:330px;
    background:radial-gradient(circle at 60% 60%, #f6b96b, #9fd3ee 55%, rgba(159,211,238,0) 72%)}
  .corner-pattern.right{right:-80px;top:-60px;width:260px;height:280px;
    background:radial-gradient(circle at 40% 45%, #f7a5c4, #f9d27a 50%, rgba(249,210,122,0) 72%)}

  .brand{position:absolute;left:105px;top:30px;display:flex;align-items:center;gap:26px}
  .brand-mark{width:160px;height:160px;border-radius:50%;background:var(--white)}
  .brand-name{line-height:1}
  .brand-name .the,.brand-name .tail{font-size:50px;font-weight:500;display:block}
  .brand-name .name{font-size:66px;font-weight:700;color:var(--magenta);display:block;margin:6px 0 8px}

  .process{position:absolute;left:0;right:0;top:245px;height:92px;
    background:linear-gradient(90deg,rgba(238,240,122,0) 0%,var(--band-yellow) 20%,var(--band-yellow) 80%,rgba(238,240,122,0) 100%);
    text-align:center;font-size:36px;line-height:42px;padding-top:4px}

  .pricing{position:absolute;left:82px;top:356px;font-family:"Oswald",sans-serif}
  .pricing-head{width:290px;height:120px;background:var(--leaf);color:var(--white);
    clip-path:polygon(0 0,100% 0,86% 100%,0 100%);font-size:50px;line-height:52px;padding:8px 0 0 10px;font-weight:600}
  .price-line{display:flex;align-items:center;gap:10px;margin-top:12px;padding-left:10px;font-family:"Cabin",sans-serif}
  .price-line strong{font-family:"Oswald",sans-serif;font-size:38px;font-weight:600}
  .price-line span{font-size:16px;line-height:18px}
  .price-line.large{width:240px;height:44px;background:var(--leaf-light);clip-path:polygon(0 0,100% 0,92% 100%,0 100%)}
  .price-line.small{width:218px;height:54px;background:var(--lime);clip-path:polygon(0 0,100% 0,92% 100%,0 100%);margin-top:10px}

  .product{position:absolute;width:150px}
  .product .tag{width:136px;height:180px;margin-left:10px;background:var(--white);
    border:6px solid var(--leaf);border-radius:22px 22px 14px 14px;transform:rotate(9deg);
    box-shadow:0 10px 14px rgba(0,0,0,.18);position:relative;padding:24px 10px 10px}
  .product .tag::before{content:"";position:absolute;top:6px;left:50%;width:14px;height:14px;margin-left:-7px;
    border:2px solid #cfcfcf;border-radius:50%}
  .product .art{width:100%;height:100%;border-radius:6px}
  .product .pn{font-size:16px;margin-top:6px;letter-spacing:.5px}

  .offer{position:absolute;left:612px;top:882px;width:226px;text-align:center}
  .offer-circle{width:126px;height:126px;margin:0 auto;border-radius:50%;background:var(--badge-yellow);
    border:2px dashed #c9c32a;font-family:"Oswald",sans-serif;line-height:1;padding-top:22px}
  .offer-circle .pct{font-size:44px;color:var(--ink);display:block}
  .offer-circle .off{font-size:34px;color:var(--ribbon-red);display:block}
  .offer-ribbon{margin-top:-6px;height:38px;background:var(--ribbon-red);color:var(--white);
    clip-path:polygon(0 0,100% 0,96% 50%,100% 100%,0 100%,4% 50%);font-size:30px;line-height:38px;font-weight:500}

  .more{position:absolute;left:0;right:0;top:1082px;text-align:center;font-size:30px}
  .contact-band{position:absolute;left:0;right:0;top:1123px;height:60px;background:var(--blue-deep);
    color:var(--white);text-align:center;font-weight:700;font-size:20px;line-height:56px}
  .contact-strip{position:absolute;left:0;right:0;top:1183px;height:17px;background:var(--blue-light)}
</style>
</head>
<body>
<main class="flyer">
  <div class="corner-pattern left" role="img" aria-label="Colourful floral paisley pattern"></div>
  <div class="corner-pattern right" role="img" aria-label="Colourful floral paisley pattern"></div>

  <header class="brand">
    <div class="brand-mark"></div>
    <h1 class="brand-name">
      <span class="the">THE</span>
      <span class="name">BRIGHT FERN</span>
      <span class="tail">STUDIO PRODUCT</span>
    </h1>
  </header>

  <p class="process">ALL OF OUR PRODUCTS ARE MADE WITH<br>HAND-ROLLED STRIPS OF PAPER</p>

  <section class="pricing">
    <div class="pricing-head">WHOLESALE<br>PRICING IS</div>
    <div class="price-line large"><strong>4$</strong><span>FOR 5"X7" CARDS &amp;</span></div>
    <div class="price-line small"><strong>2.5$</strong><span>FOR 4"X4" CARDS<br>+ SHIPPING.</span></div>
  </section>

  <div class="product" style="left:440px;top:360px"><div class="tag"><div class="art" role="img" aria-label="Quilled green tree card" style="background:linear-gradient(#3f9a2a,#7c5a36)"></div></div><p class="pn">PN. 123</p></div>
  <div class="product" style="left:636px;top:360px"><div class="tag"><div class="art" role="img" aria-label="Quilled floral elephant card" style="background:linear-gradient(135deg,#3a7fc8,#8a2f7a,#3f9a3a)"></div></div><p class="pn">PN. 123</p></div>

  <div class="product" style="left:52px;top:610px"><div class="tag"><div class="art" role="img" aria-label="Quilled autumn leaves card" style="background:linear-gradient(135deg,#f2c22a,#e2451e,#4aa32d)"></div></div><p class="pn">PN. 123</p></div>
  <div class="product" style="left:250px;top:610px"><div class="tag"><div class="art" role="img" aria-label="Quilled loon bird on water card" style="background:linear-gradient(135deg,#f2f2f2,#3a3a3a,#bfe4ee)"></div></div><p class="pn">PN. 123</p></div>
  <div class="product" style="left:436px;top:610px"><div class="tag"><div class="art" role="img" aria-label="Quilled happy birthday lettering card" style="background:linear-gradient(135deg,#f7f7f7,#c9e6d8,#f0d0d0)"></div></div><p class="pn">PN. 123</p></div>
  <div class="product" style="left:624px;top:610px"><div class="tag"><div class="art" role="img" aria-label="Quilled colourful butterfly card" style="background:linear-gradient(135deg,#f06a1e,#d6232a,#2b7fd0,#3aa34a)"></div></div><p class="pn">PN. 123</p></div>

  <div class="product" style="left:52px;top:855px"><div class="tag"><div class="art" role="img" aria-label="Quilled state outline with red heart card" style="background:linear-gradient(135deg,#e8f1e2,#3c8c3a,#d22630)"></div></div><p class="pn">PN. 123</p></div>
  <div class="product" style="left:250px;top:855px"><div class="tag"><div class="art" role="img" aria-label="Quilled blue and yellow fish card" style="background:linear-gradient(135deg,#f2f6f8,#2f78c9,#f2c42a)"></div></div><p class="pn">PN. 123</p></div>
  <div class="product" style="left:436px;top:855px"><div class="tag"><div class="art" role="img" aria-label="Quilled dragonfly card" style="background:linear-gradient(135deg,#f4f6f2,#2f7fd0,#9cc63a)"></div></div><p class="pn">PN. 123</p></div>

  <div class="offer">
    <div class="offer-circle"><span class="pct">10%</span><span class="off">OFF</span></div>
    <div class="offer-ribbon">FIRST ORDER</div>
  </div>

  <p class="more">MORE PRODUCTS WE HAVE</p>
  <footer class="contact-band">FOR MORE INFORMATION CONTACT US NOW</footer>
  <div class="contact-strip"></div>
</main>
</body>
</html>
```